New Business Card Design Project

hello again,
i have an awful year and we were not able to complete our logo plan. we would like to use our #1 logo for business card design process. the primary colors for business card should be white background with orange & black letters. our business is mobil truck cranes. we deliver heavy stuff and unload cargo with crane that is mounted on our trucks.
here is our business card info:
HARBORLINE LIFT HAULERS, INC.
482 WICKHAM AVE
LAWRENCE, NY 11597
OFFICE - 516 430 2291
DIRECT - 1 888 LIFT HAULS
GERALD@HLHAUL.EXAMPLE
PLEASE also try to get our slogan on card .... "Our Loads Keep Climbin"
lastly please also put "24 hour Knuckleboom Service"
you can call me anytime 24/7 to discuss...my cell # is: 516 907 4463
please also list: Gerald Pruitt, President
Target Market(s)
Heavy Construction industry
Industry/Entity Type
heavy construction industry
Contact Information for Business Card
24 Hr Knuckleboom Service

```html
<!DOCTYPE html>
<html lang="en">
<head>
<meta charset="utf-8">
<title>Harborline Lift Haulers – Business Card</title>
<link href="https://fonts.googleapis.com/css2?family=Montserrat:wght@500;700;800;900&display=swap" rel="stylesheet">
<style>
  :root{
    --bg:#cfcfcf;
    --orange:#f37f22;
    --black:#111111;
    --white:#ffffff;
    --rule:#d6d6d6;
  }
  *{box-sizing:border-box;margin:0;padding:0}
  html,body{width:1200px;height:852px;overflow:hidden}
  body{background:var(--bg);font-family:"Montserrat",Arial,sans-serif;position:relative}
  .card{position:absolute;width:620px;height:354px;border-radius:26px;overflow:hidden;box-shadow:0 10px 24px rgba(0,0,0,.25)}
  .card--front{left:60px;top:50px;background:var(--orange)}
  .card--back{left:520px;top:448px;background:var(--white)}

  .identity{position:absolute;text-align:center;text-transform:uppercase;color:var(--black)}
  .identity__slogan{display:block;font-weight:800;letter-spacing:.5px}
  .identity__name{display:block;font-weight:900;line-height:1.05;letter-spacing:.5px;white-space:nowrap}
  .identity__title{display:block;font-weight:700;letter-spacing:.4px}

  .card--front .identity{left:0;right:0;top:104px}
  .card--front .identity__slogan{font-size:18px;margin-bottom:8px}
  .card--front .identity__name{font-size:40px}

  .card--back .identity{left:80px;width:330px;top:42px}
  .card--back .identity__slogan{font-size:13px;color:var(--orange);margin-bottom:5px}
  .card--back .identity__name{font-size:23px}
  .card--back .identity__title{font-size:12px;margin-top:7px}

  .contact{position:absolute;font-weight:800;font-size:14px;color:var(--black);text-transform:uppercase;letter-spacing:.3px}
  .contact__icon{display:block;width:30px;height:30px}
  .contact__label{display:block;color:var(--orange);font-weight:500;font-size:14px;margin:4px 0 3px}
  .contact--email{left:428px;right:14px;top:40px;text-align:center}
  .contact--email .contact__icon{margin:0 auto}
  .contact--email .contact__value{font-size:11px;letter-spacing:.2px;white-space:nowrap}
  .contact--direct{left:270px;top:190px}
  .contact--direct .contact__icon,.contact--direct .contact__label{margin-left:28px}
  .contact--office{left:40px;top:220px}
  .address{position:absolute;left:40px;top:300px;font-weight:700;font-size:13px;line-height:1.25;color:var(--black);text-transform:uppercase}

  .divider{position:absolute;width:1px;background:var(--rule)}
  .divider--a{left:250px;top:200px;height:70px}
  .divider--b{left:420px;top:70px;height:80px}

  .service-band{position:absolute;right:0;bottom:0;width:370px;height:58px}
  .service-band svg{position:absolute;inset:0}
  .service-band__text{position:absolute;left:36px;top:20px;font-weight:800;font-size:15px;color:var(--white);text-transform:uppercase;white-space:nowrap}
  .service-band__text em{font-style:normal;color:var(--orange)}
</style>
</head>
<body>

<section class="card card--front" aria-label="Card front">
  <div class="identity">
    <span class="identity__slogan">Our Loads Keep Climbin</span>
    <span class="identity__name">Harborline<br>Lift Haulers, Inc.</span>
  </div>
</section>

<section class="card card--back" aria-label="Card back">
  <div class="identity">
    <span class="identity__slogan">Our Loads Keep Climbin</span>
    <span class="identity__name">Harborline<br>Lift Haulers, Inc.</span>
    <span class="identity__title">Gerald Pruitt, President</span>
  </div>

  <div class="divider divider--a"></div>
  <div class="divider divider--b"></div>

  <div class="contact contact--email">
    <svg class="contact__icon" viewBox="0 0 30 30" aria-hidden="true">
      <circle cx="15" cy="15" r="15" fill="var(--orange)"/>
      <rect x="8" y="10" width="14" height="10" fill="none" stroke="#fff" stroke-width="1.6"/>
      <path d="M8 10 L15 16 L22 10" fill="none" stroke="#fff" stroke-width="1.6"/>
    </svg>
    <span class="contact__label">Email</span>
    <span class="contact__value">GERALD@HLHAUL.EXAMPLE</span>
  </div>

  <div class="contact contact--direct">
    <svg class="contact__icon" viewBox="0 0 30 30" aria-hidden="true">
      <circle cx="15" cy="15" r="15" fill="var(--orange)"/>
      <rect x="10" y="7" width="10" height="16" rx="2" fill="none" stroke="#fff" stroke-width="1.6"/>
      <circle cx="15" cy="20" r="1" fill="#fff"/>
    </svg>
    <span class="contact__label">Direct</span>
    <span class="contact__value">1 888 LIFT HAULS</span>
  </div>

  <div class="contact contact--office">
    <svg class="contact__icon" viewBox="0 0 30 30" aria-hidden="true">
      <circle cx="15" cy="15" r="15" fill="var(--orange)"/>
      <path d="M8 13 Q15 7 22 13 L20 15 L18 13 L12 13 L10 15 Z" fill="#fff"/>
      <rect x="10" y="15" width="10" height="7" rx="1" fill="#fff"/>
    </svg>
    <span class="contact__label">Office</span>
    <span class="contact__value">516 430 2291</span>
  </div>

  <div class="address">482 Wickham Ave<br>Lawrence, NY 11597</div>

  <div class="service-band">
    <svg viewBox="0 0 370 58" preserveAspectRatio="none" aria-hidden="true">
      <path d="M0 58 L0 22 Q0 0 26 0 L370 0 L370 58 Z" fill="var(--black)"/>
    </svg>
    <span class="service-band__text">24 Hour <em>Knuckleboom Service</em></span>
  </div>
</section>

</body>
</html>
```